Web design required

1-We need a web design for existing company based in New Zealand
2-We build residential house and light commercial
3-We has in-house designer which allow us can provide interior design
4-We modeling project before site construction, which enable both client and construction team to visually analysis whole project,

Target Market(s)

middle class residential house market
Ref: http://www.brackwellbuilders.co.nz/

Industry/Entity Type

Construction Company

Number of Pages Required

1 page

Font styles to use
Sans Serif
Other font styles liked:
• Such as : Central Gothic or similar which has more design taste

Colors

Designer to choose colors to be used in the design.

Requirements
Must have
• Front sheet, contact information, sample project

```html
<!DOCTYPE html>
<html lang="en">
<head>
<meta charset="utf-8">
<title>Kestrel Homes</title>
<link href="https://fonts.googleapis.com/css2?family=Questrial&family=Montserrat:wght@600;700&display=swap" rel="stylesheet">
<style>
:root{
  --blue:#1f4fae;
  --blue-deep:#163d8c;
  --navy:#0d1e3f;
  --white:#ffffff;
  --ink:#2b2b2b;
  --muted:#8a8a8a;
  --grey-bg:#eef0f3;
  --footer:#2a2a2c;
  --line:#555558;
  --red:#e3263a;
}
*{margin:0;padding:0;box-sizing:border-box}
html,body{width:1200px;height:3814px;overflow:hidden}
body{position:relative;background:var(--white);font-family:"Questrial",sans-serif;color:var(--ink)}
.abs{position:absolute}
.hero-photo{left:0;top:0;width:1200px;height:640px;background:linear-gradient(180deg,#0f2350 0%,#1c3a78 45%,#7a5a3a 70%,#20355f 100%)}
.brand{left:100px;top:52px;display:flex;align-items:center;gap:12px;color:var(--white);font-size:30px;letter-spacing:1px}
.brand-mark{width:34px;height:34px;border:3px solid var(--white);border-radius:50%}
.nav a{color:var(--white);text-decoration:none;position:absolute;white-space:nowrap;font-size:15px}
.login{left:986px;top:56px;width:112px;height:36px;border:2px solid var(--white);color:var(--white);font-size:14px;display:flex;align-items:center;justify-content:center;gap:6px}
.hero-title{left:0;width:1200px;top:268px;text-align:center;color:var(--white);font-family:"Montserrat",sans-serif;font-weight:600;font-size:42px;text-shadow:0 2px 6px rgba(0,0,0,.4)}
.scroll-btn{left:580px;top:425px;width:40px;height:40px;border:2px solid var(--white);border-radius:50%}
.hex-badge{left:562px}
.section-title{font-size:40px;font-weight:400;color:var(--ink)}
.about-title{left:99px;top:760px}
.about-text{left:99px;top:822px;width:590px;font-size:14px;line-height:27px;color:var(--muted)}
.faint-build{background:linear-gradient(90deg,rgba(230,233,238,0),var(--grey-bg) 30%)}
.video-main{left:102px;top:974px;width:605px;height:317px;background:linear-gradient(180deg,#9fb6d3 0%,#dfe4ea 45%,#4f6d3a 80%,#3e5a2c 100%);box-shadow:0 6px 18px rgba(0,0,0,.2)}
.video-blue{left:658px;top:1068px;width:308px;height:274px;background:linear-gradient(135deg,#2a5bbd,#163d8c)}
.play{width:54px;height:54px;border-radius:50%;background:var(--red)}
.services-title{left:0;width:1200px;top:1532px;text-align:center;color:var(--white)}
.hex-label{fill:var(--white);font-family:"Montserrat",sans-serif;font-weight:700;font-size:18px;text-anchor:middle}
.projects-title{left:99px;top:2280px}
.card{background:var(--white);box-shadow:0 6px 14px rgba(0,0,0,.15)}
.card-photo{width:100%;height:190px}
.card-name{text-align:center;font-size:19px;padding-top:14px;color:var(--ink);white-space:nowrap}
.btn-outline{left:521px;top:2855px;width:224px;height:48px;border:2px solid var(--blue);color:var(--blue);font-family:"Montserrat",sans-serif;font-weight:700;font-size:14px;display:flex;align-items:center;justify-content:center;gap:8px}
.footer{left:0;top:3000px;width:1200px;height:814px;background:linear-gradient(180deg,#3a3a3d,var(--footer))}
.foot-head{font-family:"Montserrat",sans-serif;font-weight:700;font-size:24px;color:var(--white)}
.field{left:99px;width:351px;height:46px;background:var(--white);font-size:13px;color:var(--muted);padding:15px 14px}
.send{left:99px;top:3513px;width:351px;height:41px;background:var(--blue);color:var(--white);font-family:"Montserrat",sans-serif;font-weight:700;font-size:14px;display:flex;align-items:center;justify-content:center}
.map{left:496px;top:3251px;width:604px;height:303px;background:linear-gradient(135deg,#e6e3dc,#d3d8cf)}
.map-card{left:160px;top:196px;width:290px;padding:10px 12px;background:var(--white);font-size:12px;line-height:19px;color:#555;white-space:nowrap}
.quote{left:99px;top:3600px;display:flex;align-items:center;gap:14px;color:var(--white);font-family:"Montserrat",sans-serif;font-weight:700;font-size:24px;white-space:nowrap}
.phone-ring{width:46px;height:46px;border:2px solid var(--white);border-radius:50%;display:flex;align-items:center;justify-content:center}
.foot-nav{top:3612px;left:552px;width:548px;display:flex;justify-content:space-between;font-size:15px;color:var(--white);white-space:nowrap}
.rule{left:99px;top:3706px;width:1001px;height:1px;background:var(--line)}
.copyright{left:99px;top:3755px;font-size:12px;color:#cfcfcf}
.socials{left:938px;top:3746px;display:flex;gap:9px}
.socials span{width:33px;height:33px;border:2px solid var(--white);border-radius:50%}
</style>
</head>
<body>

<div class="abs hero-photo" role="img" aria-label="Modern home with infinity pool at dusk overlooking the harbour"></div>

<svg class="abs" style="left:0;top:480px" width="1200" height="260" viewBox="0 0 1200 260">
  <polygon points="0,20 600,140 1200,20 1200,200 600,150 0,200" fill="#1f4fae"/>
  <polygon points="0,20 600,140 600,150 0,200" fill="#163d8c" opacity="0.35"/>
  <polygon points="0,200 600,150 1200,200 1200,260 0,260" fill="#ffffff"/>
</svg>

<div class="abs brand"><span class="brand-mark"></span>KESTREL HOMES</div>
<nav class="abs nav" style="left:0;top:0">
  <a style="left:496px;top:63px">HOME</a>
  <a style="left:582px;top:63px">SERVICES</a>
  <a style="left:686px;top:63px">ABOUT</a>
  <a style="left:773px;top:63px">PROJECTS</a>
  <a style="left:885px;top:63px">CONTACT</a>
</nav>
<div class="abs login">
  <svg width="11" height="13" viewBox="0 0 11 13"><rect x="1" y="5" width="9" height="7" fill="#fff"/><path d="M3 5V3.5a2.5 2.5 0 0 1 5 0V5" stroke="#fff" stroke-width="1.5" fill="none"/></svg>LOG IN
</div>

<h1 class="abs hero-title">Welcome to Kestrel Homes</h1>
<div class="abs scroll-btn">
  <svg width="36" height="36" viewBox="0 0 36 36"><path d="M18 11v13M13 19l5 5 5-5" stroke="#fff" stroke-width="2" fill="none"/></svg>
</div>

<svg class="abs hex-badge" style="top:548px" width="76" height="80" viewBox="0 0 76 80">
  <polygon points="38,2 73,21 73,59 38,78 3,59 3,21" fill="#1f4fae" stroke="#fff" stroke-width="3"/>
</svg>

<div class="abs faint-build" style="left:700px;top:740px;width:500px;height:640px" role="img" aria-label="Faint scaffolding of a house under construction"></div>
<h2 class="abs section-title about-title">About Kestrel Homes</h2>
<p class="abs about-text">Kestrel Homes is dedicated to creating and renovating beautiful and unusual buildings. Kestrel Homes works with you to take dream houses off the blueprints and into reality. We have the knowledge and expertise to customise homes to suit you – from unusual materials and designs to environmentally sensitive locations.</p>

<div class="abs video-blue" role="img" aria-label="Blue tinted photo of a house under construction"></div>
<div class="abs play" style="left:785px;top:1178px"><svg width="54" height="54" viewBox="0 0 54 54"><polygon points="22,17 37,27 22,37" fill="#fff"/></svg></div>
<div class="abs video-main" role="img" aria-label="White two storey house with grey roof behind a hedge"></div>
<div class="abs play" style="left:377px;top:1105px"><svg width="54" height="54" viewBox="0 0 54 54"><polygon points="22,17 37,27 22,37" fill="#fff"/></svg></div>

<svg class="abs" style="left:0;top:1431px" width="1200" height="615" viewBox="0 0 1200 615">
  <polygon points="0,70 730,0 1200,70 1200,545 520,615 0,545" fill="#1f4fae"/>
</svg>
<h2 class="abs section-title services-title">Our Services</h2>
<svg class="abs" style="left:100px;top:1619px" width="1000" height="424" viewBox="0 0 1000 424">
  <defs>
    <linearGradient id="hexA" x1="0" y1="0" x2="1" y2="1"><stop offset="0" stop-color="#c9a77a"/><stop offset="1" stop-color="#1f4fae"/></linearGradient>
    <linearGradient id="hexB" x1="0" y1="0" x2="1" y2="1"><stop offset="0" stop-color="#b39572"/><stop offset="1" stop-color="#1f4fae"/></linearGradient>
    <linearGradient id="hexC" x1="0" y1="0" x2="1" y2="1"><stop offset="0" stop-color="#c97a4a"/><stop offset="1" stop-color="#1f4fae"/></linearGradient>
  </defs>
  <g role="img" aria-label="Planner reviewing drawings on a desk">
    <polygon points="167,2 332,97 332,327 167,422 2,327 2,97" fill="url(#hexA)" stroke="#fff" stroke-width="4"/>
  </g>
  <text class="hex-label" x="167" y="272">Preconstruction</text>
  <text class="hex-label" x="167" y="302">Planning</text>
  <g role="img" aria-label="Cutaway model of a house interior">
    <polygon points="500,2 665,97 665,327 500,422 335,327 335,97" fill="url(#hexB)" stroke="#fff" stroke-width="4"/>
  </g>
  <text class="hex-label" x="500" y="272">Construction</text>
  <text class="hex-label" x="500" y="302">Modelling</text>
  <g role="img" aria-label="Site managers reviewing plans on site">
    <polygon points="833,2 998,97 998,327 833,422 668,327 668,97" fill="url(#hexC)" stroke="#fff" stroke-width="4"/>
  </g>
  <text class="hex-label" x="833" y="272">Full Project</text>
  <text class="hex-label" x="833" y="302">Management</text>
</svg>

<div class="abs" style="left:0;top:2100px;width:470px;height:520px;background:linear-gradient(90deg,var(--grey-bg),rgba(238,240,243,0))" role="img" aria-label="Faint scaffolding of a house under construction"></div>
<svg class="abs" style="left:180px;top:2190px" width="70" height="74" viewBox="0 0 70 74">
  <polygon points="35,2 67,20 67,54 35,72 3,54 3,20" fill="#9fb0cf" opacity="0.7"/>
</svg>
<h2 class="abs section-title projects-title">Our Projects</h2>

<div class="abs card" style="left:490px;top:2278px;width:296px;height:256px">
  <div class="card-photo" role="img" aria-label="House under construction with scaffolding" style="background:linear-gradient(180deg,#c4ccd6,#7d8791)"></div>
  <div class="card-name">Ashford Project</div>
</div>
<div class="abs card" style="left:806px;top:2278px;width:294px;height:256px">
  <div class="card-photo" role="img" aria-label="Two storey white house with scaffolding" style="background:linear-gradient(180deg,#d7dde4,#8c8f86)"></div>
  <div class="card-name">Whitmore Project</div>
</div>
<div class="abs card" style="left:173px;top:2555px;width:290px;height:254px">
  <div class="card-photo" role="img" aria-label="Interior stairway with timber treads" style="background:linear-gradient(135deg,#8a5a32,#3a2a1e)"></div>
  <div class="card-name">Kowhai Project - Interior</div>
</div>
<div class="abs card" style="left:490px;top:2555px;width:296px;height:254px">
  <div class="card-photo" role="img" aria-label="Dark modern house facade with timber cladding" style="background:linear-gradient(180deg,#6f6f6b,#2f2e2c)"></div>
  <div class="card-name">Kowhai Project</div>
</div>
<div class="abs card" style="left:806px;top:2555px;width:294px;height:254px">
  <div class="card-photo" role="img" aria-label="White modern home lit at dusk" style="background:linear-gradient(180deg,#3a5c9a,#c9a469)"></div>
  <div class="card-name">Ridge Rd Project</div>
</div>

<div class="abs btn-outline">VIEW ALL PROJECTS
  <svg width="14" height="14" viewBox="0 0 14 14"><circle cx="7" cy="7" r="7" fill="#1f4fae"/><path d="M6 4l3 3-3 3" stroke="#fff" stroke-width="1.6" fill="none"/></svg>
</div>

<div class="abs footer" role="img" aria-label="Darkened photo of a modern home interior"></div>
<svg class="abs" style="left:0;top:2923px" width="1200" height="220" viewBox="0 0 1200 220">
  <polygon points="0,0 600,70 1200,0 1200,150 600,217 0,150" fill="#1f4fae"/>
  <polygon points="0,0 600,70 600,217 0,150" fill="#163d8c" opacity="0.4"/>
</svg>
<svg class="abs hex-badge" style="top:2998px" width="76" height="80" viewBox="0 0 76 80">
  <polygon points="38,2 73,21 73,59 38,78 3,59 3,21" fill="#1f4fae" stroke="#fff" stroke-width="3"/>
</svg>

<div class="abs foot-head" style="left:99px;top:3198px">CONTACT FORM</div>
<div class="abs field" style="top:3251px">Name</div>
<div class="abs field" style="top:3307px">Phone No.</div>
<div class="abs field" style="top:3363px">Email Id *</div>
<div class="abs field" style="top:3419px;height:89px">Message</div>
<div class="abs send">SEND MESSAGE</div>

<div class="abs foot-head" style="left:496px;top:3198px">LOCATION</div>
<div class="abs map" role="img" aria-label="Street map showing the office location">
  <svg class="abs" style="left:296px;top:92px" width="22" height="30" viewBox="0 0 22 30"><path d="M11 0a11 11 0 0 1 11 11c0 8-11 19-11 19S0 19 0 11A11 11 0 0 1 11 0z" fill="#e3263a"/><circle cx="11" cy="11" r="4" fill="#fff"/></svg>
  <div class="abs map-card">18 Harbourview Lane, Eastfield Auckland<br>Tel: 0064 9 555 0147<br>Email: info@kestrelhomes.co.nz</div>
</div>

<div class="abs quote">
  <span class="phone-ring"><svg width="20" height="20" viewBox="0 0 24 24"><path d="M6.6 10.8a15 15 0 0 0 6.6 6.6l2.2-2.2a1 1 0 0 1 1-.25 11.4 11.4 0 0 0 3.6.57 1 1 0 0 1 1 1V20a1 1 0 0 1-1 1A17 17 0 0 1 3 4a1 1 0 0 1 1-1h3.5a1 1 0 0 1 1 1c0 1.25.2 2.45.57 3.6a1 1 0 0 1-.25 1z" fill="#fff"/></svg></span>
  GET A QUOTE: 09 555 0147
</div>
<nav class="abs foot-nav">
  <span>HOME</span><span>/</span><span>SERVICES</span><span>/</span><span>ABOUT</span><span>/</span><span>PROJECTS</span><span>/</span><span>CONTACT</span>
</nav>
<div class="abs rule"></div>
<div class="abs copyright">© copyright 2017 by Kestrel Homes. All Rights reserved</div>
<div class="abs socials"><span></span><span></span><span></span><span></span></div>

</body>
</html>
```